Redesign a programmers open source website

This is a fairly old website (started 1999) that hosts lots of programming-related stuff, from the useful (freeware tools, articles on programming topics) to the obscure (esoteric programming languages, tips on code obfuscation and bad examples), plus a couple of other bits thrown in. It is 100% open source and free. However, it looks a bit boring, so I want to liven up the design, and make it the basis for a future portfolio showcase. The design should be compatible with bootstrap (i.e. work on mobile devices).

Take a look at the existing one over at
vorlzarchive.net

Target Market(s)

Software Companies

Coding

Coded - Design and coding required

Number of Pages Required

2 page

Font styles to use
Sans Serif

Requirements
Must have
• After reviewing the designs submitted so far:
• - something reduced and elegant
• - something that is not too noisy, but instead reflects quality.
• - I would like to see two pages: the frontpage, and one text-heavy (for example, an article on one of my programming languages).

```html
<!DOCTYPE html>
<html lang="en">
<head>
<meta charset="utf-8">
<title>Vorlz Archive – Programming</title>
<link rel="stylesheet" href="https://fonts.googleapis.com/css2?family=Roboto:wght@400;500&family=Open+Sans:wght@400&family=Cousine&display=swap">
<style>
:root{
  --brand:#0a56a8;
  --brand-line:#5d8fcb;
  --accent:#ef8a1f;
  --text:#6a6a6a;
  --item-text:#555a60;
  --code-bg:#3b4149;
  --code-text:#c9ccd0;
  --item-border:#d6d6d6;
  --item-top:#ffffff;
  --item-bottom:#f1f1f1;
  --icon:#4e5358;
}
*{box-sizing:border-box;margin:0;padding:0}
html,body{width:1200px;height:2344px;overflow:hidden;background:#fff}
body{position:relative;font-family:"Open Sans",Arial,sans-serif;color:var(--text)}
.site-header{height:91px;background:var(--brand);position:relative}
.brand{position:absolute;left:97px;top:25px;font-family:"Roboto",Arial,sans-serif;font-weight:500;font-size:29px;color:#fff;letter-spacing:.2px}
.main-nav{position:absolute;top:33px;left:567px;display:flex}
.main-nav a{display:block;height:33px;line-height:31px;padding:0 10px;font-family:"Roboto",Arial,sans-serif;font-size:12.5px;color:#e6eefa;text-decoration:none;margin-right:21px;border:1px solid transparent}
.main-nav a.active{border-color:var(--brand-line);color:#fff}
.content{position:absolute;left:180px;top:91px;width:836px}
.section-title{font-family:"Roboto",Arial,sans-serif;font-weight:400;font-size:30px;color:var(--accent);margin-top:49px;line-height:38px}
.intro{font-size:12.2px;line-height:23px;margin-top:14px}
.intro+.intro{margin-top:8px}
.code-block{background:var(--code-bg);border-radius:3px;margin-top:15px;height:356px;padding:27px 32px;font-family:"Cousine",monospace;font-size:12px;line-height:22.2px;color:var(--code-text);white-space:pre}
.code-note{font-size:12.2px;margin-top:12px}
.accordion{list-style:none;margin-top:26px}
.accordion li{height:53px;margin-bottom:16px;border:1px solid var(--item-border);border-radius:2px;background:linear-gradient(var(--item-top),var(--item-bottom));display:flex;align-items:center;padding-left:20px;font-family:"Roboto",Arial,sans-serif;font-size:19px;color:var(--item-text)}
.accordion li.spaced{margin-top:8px}
.accordion svg{width:18px;height:18px;margin-right:14px;flex:none}
.second-title{margin-top:84px}
.accordion.second{margin-top:8px}
.site-footer{position:absolute;left:0;top:2203px;width:1200px;height:141px;background:var(--brand);color:#fff}
.footer-links{position:absolute;left:99px;top:50px;font-size:9.6px;word-spacing:2px}
.footer-links span{margin:0 5px}
.copyright{position:absolute;left:99px;top:78px;font-size:9.6px}
.social{position:absolute;left:999px;top:57px;display:flex;gap:5px}
.social span{width:30px;height:30px;border-radius:50%;border:2px solid #fff;display:block}
.social .s1{background:#3b5b9a}
.social .s2{background:#2aa5d9}
.social .s3{background:#6aa33a;display:flex;align-items:center;justify-content:center}
</style>
</head>
<body>
<header class="site-header">
  <div class="brand">Vorlz Archive</div>
  <nav class="main-nav">
    <a class="active">Programming</a><a>Languages</a><a>Obfuscation</a><a>Downloads</a><a>Interests</a>
  </nav>
</header>

<main class="content">
  <h1 class="section-title">Making sense of STL &lt;ratio&gt;</h1>
  <p class="intro">Note: this is just one article in a series discussing the STL headers. In particular, reading the first article in the series might be helpful, as it introduces a bunch of standard techniques.</p>
  <p class="intro">Today we are going to look at something rather different: handling integer fractions in templates, courtesy of ratio. We start up with the usual boilerplate stuff:</p>
  <div class="code-block">// ratio standard header
#pragma once
#ifndef _RATIO_
#define _RATIO_
#ifndef RC_INVOKED
#include &lt;stdint.h&gt;
#include &lt;type_traits&gt;

 #pragma pack(push,_CRT_PACKING)
 #pragma warning(push,3)
 #pragma push_macro("new")
 #undef new

_STD_BEGIN</div>
  <p class="code-note">Nothing unsurprising, if you've read the previous installments of this series.</p>

  <ul class="accordion">
    <li><svg viewBox="0 0 18 18"><circle cx="9" cy="9" r="8" fill="var(--icon)"/><path d="M9 4.5v9M4.5 9h9" stroke="#fff" stroke-width="2.2"/></svg>Getting the absolute value in a template</li>
    <li><svg viewBox="0 0 18 18"><circle cx="9" cy="9" r="8" fill="var(--icon)"/><path d="M9 4.5v9M4.5 9h9" stroke="#fff" stroke-width="2.2"/></svg>How to detect overflow on multiplication in a template</li>
    <li><svg viewBox="0 0 18 18"><circle cx="9" cy="9" r="8" fill="var(--icon)"/><path d="M9 4.5v9M4.5 9h9" stroke="#fff" stroke-width="2.2"/></svg>How to detect overflow on addition of two numeric values in a template</li>
    <li><svg viewBox="0 0 18 18"><circle cx="9" cy="9" r="8" fill="var(--icon)"/><path d="M9 4.5v9M4.5 9h9" stroke="#fff" stroke-width="2.2"/></svg>The GCD (Greatest Common Denominator), in templates, without overflow</li>
    <li><svg viewBox="0 0 18 18"><circle cx="9" cy="9" r="8" fill="var(--icon)"/><path d="M9 4.5v9M4.5 9h9" stroke="#fff" stroke-width="2.2"/></svg>The actual ratio template</li>
    <li><svg viewBox="0 0 18 18"><circle cx="9" cy="9" r="8" fill="var(--icon)"/><path d="M9 4.5v9M4.5 9h9" stroke="#fff" stroke-width="2.2"/></svg>Verifying that two template arguments are of a specific type</li>
    <li><svg viewBox="0 0 18 18"><circle cx="9" cy="9" r="8" fill="var(--icon)"/><path d="M9 4.5v9M4.5 9h9" stroke="#fff" stroke-width="2.2"/></svg>Simple ratio math in templates</li>
    <li><svg viewBox="0 0 18 18"><circle cx="9" cy="9" r="8" fill="var(--icon)"/><path d="M9 4.5v9M4.5 9h9" stroke="#fff" stroke-width="2.2"/></svg>Some comparison operators</li>
    <li class="spaced"><svg viewBox="0 0 18 18"><circle cx="9" cy="9" r="8" fill="var(--icon)"/><path d="M9 4.5v9M4.5 9h9" stroke="#fff" stroke-width="2.2"/></svg>SI units in templates</li>
    <li><svg viewBox="0 0 18 18"><circle cx="9" cy="9" r="8" fill="var(--icon)"/><path d="M9 4.5v9M4.5 9h9" stroke="#fff" stroke-width="2.2"/></svg>Lessons learnt</li>
  </ul>

  <h2 class="section-title second-title">Finding the maximum profit in a shareprice array</h2>
  <ul class="accordion second">
    <li><svg viewBox="0 0 18 18"><circle cx="9" cy="9" r="8" fill="var(--icon)"/><path d="M9 4.5v9M4.5 9h9" stroke="#fff" stroke-width="2.2"/></svg>Ask yourself: Do I understand the problem?</li>
    <li><svg viewBox="0 0 18 18"><circle cx="9" cy="9" r="8" fill="var(--icon)"/><path d="M9 4.5v9M4.5 9h9" stroke="#fff" stroke-width="2.2"/></svg>Setting up a test harness</li>
    <li><svg viewBox="0 0 18 18"><circle cx="9" cy="9" r="8" fill="var(--icon)"/><path d="M9 4.5v9M4.5 9h9" stroke="#fff" stroke-width="2.2"/></svg>Brute-Force approach</li>
    <li><svg viewBox="0 0 18 18"><circle cx="9" cy="9" r="8" fill="var(--icon)"/><path d="M9 4.5v9M4.5 9h9" stroke="#fff" stroke-width="2.2"/></svg>Using Divide &amp; Conquer</li>
    <li><svg viewBox="0 0 18 18"><circle cx="9" cy="9" r="8" fill="var(--icon)"/><path d="M9 4.5v9M4.5 9h9" stroke="#fff" stroke-width="2.2"/></svg>Using One-Pass Sweep</li>
    <li><svg viewBox="0 0 18 18"><circle cx="9" cy="9" r="8" fill="var(--icon)"/><path d="M9 4.5v9M4.5 9h9" stroke="#fff" stroke-width="2.2"/></svg>Other strategies</li>
    <li><svg viewBox="0 0 18 18"><circle cx="9" cy="9" r="8" fill="var(--icon)"/><path d="M9 4.5v9M4.5 9h9" stroke="#fff" stroke-width="2.2"/></svg>But how does it actually perform?</li>
    <li><svg viewBox="0 0 18 18"><circle cx="9" cy="9" r="8" fill="var(--icon)"/><path d="M9 4.5v9M4.5 9h9" stroke="#fff" stroke-width="2.2"/></svg>Abstraction time: from int to arbitrary objects</li>
    <li><svg viewBox="0 0 18 18"><circle cx="9" cy="9" r="8" fill="var(--icon)"/><path d="M9 4.5v9M4.5 9h9" stroke="#fff" stroke-width="2.2"/></svg>Generalizing the One-Pass Sweep function</li>
  </ul>
</main>

<footer class="site-footer">
  <div class="footer-links">Home<span>|</span>Programming<span>|</span>Languages<span>|</span>Obfuscation<span>|</span>Downloads<span>|</span>Interests</div>
  <div class="copyright">Copyright &copy; 2015 &nbsp;Vorlz Archive &nbsp;&nbsp;All rights reserved.</div>
  <div class="social">
    <span class="s1" role="img" aria-label="Social link"></span>
    <span class="s2" role="img" aria-label="Social link"></span>
    <span class="s3" role="img" aria-label="Email"><svg width="14" height="10" viewBox="0 0 14 10"><rect x=".5" y=".5" width="13" height="9" fill="#fff"/><path d="M1 1l6 5 6-5" fill="none" stroke="#6aa33a" stroke-width="1.3"/></svg></span>
  </div>
</footer>
</body>
</html>
```